Maskottchen für Supplements und laborbasierte Tests im Bereich Longevity
Zielgruppe
Supplements und laborbasierte Tests im Bereich Longevity
Aufgabenstellung
Bitte an den Farben vom angehängten Logo orientieren für das Maskottchen, gerne ein Tier nehmen das für Langlebigkeit steht . Gern sehr kreativ oder auch futuristisch

```html
<!DOCTYPE html>
<html lang="de">
<head>
<meta charset="utf-8">
<title>Ewige Zyklen – Zellvera</title>
<link href="https://fonts.googleapis.com/css2?family=Montserrat:ital,wght@0,400;0,500;0,700;0,800;1,700&display=swap" rel="stylesheet">
<style>
  :root {
    --ink: #0f3d47;
    --text: #1d1d1d;
    --lime: #9bc21e;
    --teal: #1b6f80;
    --teal-light: #6fb9c4;
    --mint: #7fd35a;
    --paper: #ffffff;
  }
  * { margin: 0; padding: 0; box-sizing: border-box; }
  html, body { width: 1200px; height: 674px; overflow: hidden; background: var(--paper); }
  .slide {
    position: relative;
    width: 1200px;
    height: 674px;
    background: var(--paper);
    font-family: "Montserrat", sans-serif;
    color: var(--text);
  }
  .brand {
    position: absolute;
    top: 40px;
    right: 34px;
    display: flex;
    align-items: center;
    gap: 10px;
  }
  .brand-dot {
    width: 14px;
    height: 14px;
    border-radius: 50%;
    background: var(--lime);
  }
  .brand-name {
    font-family: "Montserrat", sans-serif;
    font-weight: 700;
    font-size: 28px;
    color: var(--ink);
    letter-spacing: -0.3px;
  }
  .headline {
    position: absolute;
    left: 118px;
    top: 110px;
    display: flex;
    align-items: center;
    gap: 12px;
    font-weight: 800;
    font-size: 39px;
    color: var(--ink);
    letter-spacing: -0.5px;
  }
  .headline-pill {
    background: var(--lime);
    color: var(--paper);
    border-radius: 14px;
    padding: 2px 12px 6px;
    line-height: 1.1;
  }
  .subline {
    position: absolute;
    left: 118px;
    top: 180px;
    font-weight: 700;
    font-size: 21px;
    color: var(--lime);
  }
  .intro {
    position: absolute;
    left: 118px;
    top: 220px;
    width: 465px;
    font-size: 13px;
    font-weight: 500;
    line-height: 26.3px;
  }
  .quote {
    position: absolute;
    left: 118px;
    top: 453px;
    padding-left: 30px;
    font-style: italic;
    font-weight: 700;
    font-size: 12.5px;
    line-height: 26.3px;
  }
  .quote::before {
    content: "";
    position: absolute;
    left: 0;
    top: 3px;
    width: 6px;
    height: 70px;
    background: linear-gradient(to bottom, var(--lime), var(--ink));
  }
  .mascot {
    position: absolute;
    left: 690px;
    top: 240px;
    width: 375px;
    height: 415px;
    border-radius: 48% 48% 30% 30% / 40% 40% 25% 25%;
    background: radial-gradient(ellipse at 50% 30%, var(--teal-light) 0%, var(--teal) 45%, rgba(127, 211, 90, 0.35) 75%, rgba(255,255,255,0) 100%);
  }
</style>
</head>
<body>
<main class="slide">
  <header class="brand">
    <span class="brand-dot"></span>
    <span class="brand-name">Zellvera</span>
  </header>

  <h1 class="headline">Ewige <span class="headline-pill">Zyklen</span></h1>
  <h2 class="subline">Symbol für Unsterblichkeit</h2>

  <p class="intro">Turritopsis dohrnii – die „unsterbliche Qualle“ – besitzt die einzigartige Fähigkeit, ihren Lebenszyklus zurückzusetzen und sich selbst zu verjün­gen. Dieses außergewöhnliche biologisch regenerierende Prinzip macht sie zu einem faszinierenden Sinnbild für Longevity, Zellgesundheit und wissenschaftliche Erneuerung. Ihr futuristisch-organischer Stil verbindet Forschung, Energie und evolutionäre Resilienz zu einem eindrucksvollen Markenmotiv.</p>

  <blockquote class="quote">
    Wahre Verjüngung beginnt dort,<br>
    wo Natur und Wissenschaft einen<br>
    neuen Zyklus des Lebens eröffnen.
  </blockquote>

  <div class="mascot" role="img" aria-label="Illustration des Maskottchens: türkisfarbene Qualle mit DNA-Doppelhelix im Schirm und grünen, geschwungenen Tentakeln"></div>
</main>
</body>
</html>
```